We need a web design for a new hair care company that is based in Israel but exports its line of products around the world. We would like special features on this website that include video, sliders and other exciting effects. The final design should present information about the products and an exciting inviting image. We also will need to know how to update the site.

Designers can look at our current website and see the colors and look of the products as well. Please go to: http://velorintresses.com

We would like to use the colors of the Velorin Tress care line of products. Wordpress seems to be a good choice. We would like four pages: Home, About Us, Contact and Products.

If designers have specific questions.....please let us know!
Let the designs begin!!!!
We are waiting and excited!

Target Market(s)

Potential haircare distributors and general public

Industry/Entity Type

Hair

Requirements
Must have
• The website must have general info about what the company is, with a video, explain how to use each product and a focus on women and hair.
Nice to have
• On the website should be the logo, product info, upbeat music, video and sliders that show the exciting world of Velorin Tresscare. It's uniqueness is that it offers Dead Sea minerals for the hair, the first of its kind.

```html
<!DOCTYPE html>
<html lang="en">
<head>
<meta charset="utf-8">
<title>About Us – Velorin Tresscare</title>
<link rel="stylesheet" href="https://fonts.googleapis.com/css2?family=Open+Sans:wght@400;600;700&display=swap">
<style>
  :root {
    --white: #ffffff;
    --ink: #2a1a0e;
    --body-text: #3a2414;
    --page-side: #b8966a;
    --page-column: #c6a67b;
    --nav-brown: #5a2e12;
    --deep-brown: #4e270f;
    --pattern-brown: #7a4a26;
    --pattern-cyan: #3fbfde;
    --logo-cyan: #3dbfe0;
    --photo-dark: #4a2e1c;
    --photo-light: #e9e4df;
  }
  * { box-sizing: border-box; margin: 0; padding: 0; }
  html, body { width: 1200px; height: 900px; overflow: hidden; background: var(--white); }
  body { position: relative; font-family: "Open Sans", Arial, sans-serif; color: var(--ink); }

  .board-title {
    position: absolute; top: 38px; left: 0; width: 1200px;
    text-align: center; font-size: 30px; font-weight: 400; letter-spacing: 0.5px; color: #111;
  }

  .site { position: absolute; left: 0; top: 100px; width: 1200px; height: 750px; background: var(--page-side); overflow: hidden; }

  .header-pattern {
    position: absolute; left: 0; top: 0; width: 1200px; height: 76px;
    background: linear-gradient(90deg, var(--pattern-brown) 0%, #9a6a3c 30%, var(--pattern-cyan) 55%, #8a5a30 80%, var(--pattern-brown) 100%);
  }
  .nav-bar { position: absolute; left: 0; top: 76px; width: 1200px; height: 40px; background: var(--nav-brown); }

  .main-nav { position: absolute; left: 474px; top: 76px; height: 40px; display: flex; align-items: center; }
  .main-nav a {
    color: var(--white); text-decoration: none; font-size: 13px; font-weight: 400;
    padding: 0 14px; border-left: 1px solid rgba(255,255,255,0.75); line-height: 16px;
  }
  .main-nav a:first-child { border-left: none; padding-left: 8px; }
  .main-nav a.is-current { color: var(--logo-cyan); }

  .content-column { position: absolute; left: 176px; top: 116px; width: 920px; height: 634px; background: var(--page-column); }

  .brand-box {
    position: absolute; left: 200px; top: 0; width: 264px; height: 184px;
    background: var(--logo-cyan); display: flex; align-items: center; justify-content: center;
    box-shadow: 0 4px 8px rgba(0,0,0,0.25);
  }
  .brand-name { font-size: 40px; font-weight: 600; color: var(--deep-brown); }

  .section-tab {
    position: absolute; left: 180px; top: 216px; width: 230px; height: 36px;
    background: var(--deep-brown); color: var(--white);
    font-size: 24px; font-weight: 400; line-height: 36px; padding-left: 34px;
  }

  .contact-line { position: absolute; top: 214px; display: flex; align-items: center; font-size: 15px; font-weight: 700; color: var(--ink); }
  .contact-line svg { margin-right: 12px; }
  .contact-email { left: 532px; }
  .contact-phone { left: 788px; }

  .hero-photo {
    position: absolute; left: 212px; top: 272px; width: 452px; height: 452px;
    background: radial-gradient(circle at 45% 40%, #8a5a3a 0%, var(--photo-dark) 45%, var(--photo-light) 85%);
  }

  .about-copy {
    position: absolute; left: 702px; top: 320px; width: 328px;
    font-size: 13px; line-height: 18px; color: var(--body-text); text-align: justify;
  }
  .about-copy p + p { margin-top: 18px; }

  .product-photo {
    position: absolute; left: 770px; top: 576px; width: 194px; height: 148px;
    background: linear-gradient(135deg, #7a3a1a 0%, #b0652e 45%, #3a1f12 100%);
    border-radius: 6px;
  }
</style>
</head>
<body>
  <h1 class="board-title">ABOUT US</h1>

  <div class="site">
    <div class="header-pattern" role="img" aria-label="Decorative paisley pattern band in brown and cyan"></div>
    <div class="nav-bar"></div>

    <nav class="main-nav">
      <a href="#">Home</a>
      <a href="#" class="is-current">About Us</a>
      <a href="#">Our Products</a>
      <a href="#">Lookbook</a>
      <a href="#">Video</a>
      <a href="#">Contact Us</a>
    </nav>

    <div class="content-column"></div>

    <div class="brand-box"><span class="brand-name">Velorin</span></div>

    <h2 class="section-tab">About Us</h2>

    <div class="contact-line contact-email">
      <svg width="34" height="20" viewBox="0 0 34 20" aria-hidden="true">
        <rect x="1" y="1" width="32" height="18" fill="none" stroke="#fff" stroke-width="2"/>
        <polyline points="1,1 17,12 33,1" fill="none" stroke="#fff" stroke-width="2"/>
      </svg>
      <span>info@velorintresses.com</span>
    </div>

    <div class="contact-line contact-phone">
      <svg width="34" height="34" viewBox="0 0 34 34" aria-hidden="true">
        <circle cx="17" cy="17" r="15" fill="none" stroke="#fff" stroke-width="2"/>
        <path d="M11 9 l4 0 l2 5 l-3 2 q2 4 6 6 l2-3 l5 2 l0 4 q-10 1 -16-16z" fill="#fff"/>
      </svg>
      <span>Call Us Now: 555.014.2738</span>
    </div>

    <div class="hero-photo" role="img" aria-label="Portrait of a woman with long, glossy dark brown hair on a white background"></div>

    <div class="about-copy">
      <p>Velorin Tresscare products are the first in the world to introduce Dead Sea Minerals to your hair! Velorin's natural formula nourish and restore hair, leaving each strand, feeling soft, silky, healthy and vibrant.</p>
      <p>Description<br>Velorin Tresscare products are unique in the beauty world. The formulas are an organic mixture of 26 revitalizing minerals only found in the Dead Sea blended with oils from the Argan nut. Velorin Tresscare combines the oils from the exotic Argan nut, or as some call it, liquid gold, is an ancient tradition that requires time and hard work.</p>
    </div>

    <div class="product-photo" role="img" aria-label="Hair care product bottles, box and jar in brown and copper packaging"></div>
  </div>
</body>
</html>
```